harbor glow security & electric needs a business card

Must be attractive and modern, look professional and upscale!!
We provide alarm and cameras services and 24 hour monitoring for commercial and residential clients. In addition, the owner is a master electrician that provides services to commercial and residential clients.
We also install and service automatic gates. We previously had two different businesses but decided to merge into one, thus creating Harbor Glow Security & Electric.

Target Market(s)

Commercial Business and residential customers

Industry/Entity Type

Security

Contact Information for Business Card

Front and back design with logo and services listed

Font styles to use
Sans Serif

Colors
ec1f27
0355a3
fbee3f

Requirements
Must have
• Front of card:
• Warren Kettleby-Owner
• telephone icon and then the number 936-555-0193
• Mail icon and then email address wkettleby@mailnook.example
• World Icon then website www.yourharborglowtx.example
• Location marker and then Marrowfield, Texas
• We would like to have a picture of the logo at least on the front
• Also need motto on front: We're There When You're Not
• The front of the card must also say Licensed and Insured in addition to:
• License Number: K47319
• TECL: 58617
• On the Back of the Card:
• List each of these Services with check marks:
• Residential and Commercial Electrical Services
• Electric Gates
• Alarm Systems
• Alarm Monitoring
• Cameras
• ***Use separate attached logo, the business card design is just to be used as a model***
Nice to have
• It would be nice to have the logo on back of the card in addition to these words at the bottom:
• "No job too big or small, we do it all!"
Should not have
• Anything crazy!!

```html
<!DOCTYPE html>
<html lang="en">
<head>
<meta charset="utf-8">
<title>Harbor Glow Security &amp; Electric – Business Card</title>
<link rel="stylesheet" href="https://fonts.googleapis.com/css2?family=Exo+2:wght@500;600;700;800&display=swap">
<style>
  :root {
    --red: #e8232b;
    --navy: #263f80;
    --ink: #1f2f5c;
    --paper: #ffffff;
    --backdrop: #e6e7ea;
  }
  * { margin: 0; padding: 0; box-sizing: border-box; }
  html, body {
    width: 1200px; height: 800px; overflow: hidden;
    background: var(--backdrop);
    font-family: "Exo 2", sans-serif;
  }
  .canvas {
    position: relative; width: 1200px; height: 800px;
    display: flex; align-items: center; justify-content: center; gap: 60px;
  }
  .card {
    position: relative; width: 520px; height: 298px;
    background: var(--paper);
    box-shadow: 0 10px 28px rgba(30, 35, 50, .16);
    overflow: hidden;
  }

  /* ---------- back ---------- */
  .back-brand {
    position: absolute; left: 40px; top: 92px; width: 150px;
    display: flex; flex-direction: column; align-items: flex-start; gap: 10px;
  }
  .brand-mark { width: 26px; height: 26px; border-radius: 50%; background: var(--red); flex: none; }
  .brand-name {
    font-weight: 700; color: var(--navy); font-size: 20px; line-height: 1.1;
  }
  .back-rule {
    position: absolute; left: 200px; top: 104px; width: 1.5px; height: 86px;
    background: var(--navy);
  }
  .service-list {
    position: absolute; left: 214px; top: 108px;
    list-style: none; color: var(--navy);
    font-size: 12.5px; font-weight: 600; line-height: 1.32;
    white-space: nowrap;
  }

  /* ---------- front ---------- */
  .front-brand {
    position: absolute; left: 220px; top: 28px;
    display: flex; align-items: center; gap: 10px;
  }
  .front-brand .brand-name { font-size: 21px; }
  .brand-rule {
    position: absolute; left: 220px; top: 90px; width: 270px; height: 1.5px;
    background: var(--red);
  }
  .holder { position: absolute; left: 220px; top: 98px; width: 270px; text-align: center; }
  .holder-name { color: var(--navy); font-weight: 700; font-size: 18px; letter-spacing: .5px; }
  .holder-role { color: var(--red); font-weight: 600; font-size: 12px; letter-spacing: 1px; }

  .top-rule {
    position: absolute; left: 0; top: 18px; width: 200px; height: 1.5px; background: var(--navy);
  }
  .contact-list {
    position: absolute; left: 18px; top: 30px; list-style: none;
    color: var(--ink); font-size: 12.5px; font-weight: 600; white-space: nowrap;
  }
  .contact-list li { display: flex; align-items: center; gap: 6px; height: 19px; }
  .contact-icon {
    width: 13px; height: 13px; flex: none; background: var(--red); border-radius: 2px;
    display: flex; align-items: center; justify-content: center;
  }
  .contact-icon svg { width: 9px; height: 9px; }

  .motto-rule {
    position: absolute; left: 0; top: 112px; width: 200px; height: 1.5px; background: var(--red);
  }
  .motto {
    position: absolute; left: 28px; top: 160px;
    color: var(--red); font-weight: 700; font-size: 15px; letter-spacing: .4px;
  }
  .license {
    position: absolute; right: 26px; top: 168px; text-align: right;
    color: var(--ink); font-size: 13px; font-weight: 600; line-height: 1.35;
  }
  .license .value { color: var(--red); }
  .license-line {
    position: absolute; left: 210px; top: 216px; width: 150px; height: 1.5px; background: var(--red);
  }
  .license-line::after {
    content: ""; position: absolute; right: -3px; top: -2.5px;
    width: 6px; height: 6px; border-radius: 50%; background: var(--red);
  }
  .insured-tag {
    position: absolute; right: 26px; top: 206px;
    background: var(--red); color: #fff; border-radius: 5px;
    padding: 5px 9px; display: flex; align-items: center; gap: 7px;
    font-size: 10px; font-weight: 700; line-height: 1.05; text-align: center;
  }
  .insured-tag small { display: block; font-size: 7px; font-weight: 600; }
  .insured-tag svg { width: 18px; height: 18px; }

  .edge-band { position: absolute; left: 0; bottom: 0; width: 100%; height: 22px; display: flex; }
  .edge-band .red { width: 46%; background: var(--red); }
  .edge-band .navy { flex: 1; background: var(--navy); }
</style>
</head>
<body>
<main class="canvas">

  <section class="card card-back" aria-label="Card back">
    <div class="back-brand">
      <span class="brand-mark"></span>
      <span class="brand-name">Harbor Glow Security &amp; Electric</span>
    </div>
    <div class="back-rule"></div>
    <ul class="service-list">
      <li>Residential and Commercial Electrical Services</li>
      <li>Electric Gates</li>
      <li>Alarm Systems</li>
      <li>Alarm Monitoring</li>
      <li>Cameras</li>
    </ul>
  </section>

  <section class="card card-front" aria-label="Card front">
    <div class="top-rule"></div>
    <ul class="contact-list">
      <li><span class="contact-icon"><svg viewBox="0 0 10 10"><path d="M2 1l2 2-1 1c.6 1.3 1.7 2.4 3 3l1-1 2 2-1.5 1.5C4.5 9.5.5 5.5 .5 2.5z" fill="#fff"/></svg></span>936-555-0193</li>
      <li><span class="contact-icon"><svg viewBox="0 0 10 10"><rect x="1" y="2.5" width="8" height="5.5" fill="none" stroke="#fff"/><path d="M1 2.5l4 3 4-3" fill="none" stroke="#fff"/></svg></span>wkettleby@mailnook.example</li>
      <li><span class="contact-icon"><svg viewBox="0 0 10 10"><circle cx="5" cy="5" r="4" fill="none" stroke="#fff"/><ellipse cx="5" cy="5" rx="1.8" ry="4" fill="none" stroke="#fff" stroke-width=".8"/><path d="M1 5h8" stroke="#fff" stroke-width=".8"/></svg></span>www.yourharborglowtx.example</li>
      <li><span class="contact-icon"><svg viewBox="0 0 10 10"><path d="M5 9.5S1.8 6 1.8 4a3.2 3.2 0 016.4 0C8.2 6 5 9.5 5 9.5z" fill="#fff"/><circle cx="5" cy="4" r="1.2" fill="#e8232b"/></svg></span>Marrowfield, Texas</li>
    </ul>
    <div class="motto-rule"></div>

    <div class="front-brand">
      <span class="brand-mark"></span>
      <span class="brand-name">Harbor Glow<br>Security &amp; Electric</span>
    </div>
    <div class="brand-rule"></div>
    <div class="holder">
      <div class="holder-name">WARREN KETTLEBY</div>
      <div class="holder-role">OWNER</div>
    </div>

    <p class="motto">WE'RE THERE WHEN YOU'RE NOT</p>

    <div class="license">
      License Number: <span class="value">K47319</span><br>
      TECL: <span class="value">58617</span>
    </div>
    <div class="license-line"></div>
    <div class="insured-tag">
      <svg viewBox="0 0 20 20"><rect x="1.5" y="1.5" width="17" height="17" rx="3" fill="none" stroke="#fff" stroke-width="1.8"/><path d="M5.5 10l3 3 6-6.5" fill="none" stroke="#fff" stroke-width="2"/></svg>
      <span>LICENSED<small>and</small>INSURED</span>
    </div>

    <div class="edge-band"><span class="red"></span><span class="navy"></span></div>
  </section>

</main>
</body>
</html>
```